Wren Automotive Detailing Flyer Design

Hi, I need a flyer design for the pricing and package display of my business (Wren Automotive Detailing)

www.plumebook.example/wrenautodetail

To keep this short and simple, I will need 2 versions of your finished product, can be similar in design just has to be saying something different.

First flyer will be the general version for all customers.

It will need to include the following!
Format, Placement, Font, Design etc.. is all up to you!

==================================

Package 1 [Cars $49.99][Trucks Vans & SUV's $54.99]: Speed Detail

- Exterior Pressure Clean w/ Spotless water
treatment and Vacuum dried
- Wheel Wells Glossed and Cleaned
- Tires Cleaned and Hand Dried
- Tires Dressed with Gloss Finish
- Exterior and Interior Windows cleaned and Hand Dried
- Interior is Vacuumed and Door jams cleaned to Perfection!

Package 2 [Cars $59.99][Trucks Vans & SUV's $64.99]: Speed Detail & Hand Waxing

- Exterior Pressure Clean w/ Spotless water treatment and Vacuum dried
- Hand Applied Wax Treatment with Halvern's Advanced Spray on wax & Micro Scratch Sealant!

Package 3 [Cars $110.00][Trucks Vans & SUV's $149.99]: Advanced Interior Detail

- Interior & Exterior Windows Cleaned and Hand Dried
- All Vents and Creases cleaned out
- Advanced plastic/vinyl/leather Vexamor Interior Treatment!
- Plastic/Vinyl/Leather Conditioner Vexamor Treatment
- Hand Treated Dust Removal
- Seats/Carpets/Headliner steam cleaned
- Seat Belts/Trunks & Floor Mats Treated and Rejuvenated
- Stain Removal

Package 4 [Cars $110.00][Trucks Vans & SUV's $149.99]: Advanced Exterior Detail

- Exterior Pressure Clean w/ Spotless water treatment and Vacuum dry with additional Hand Drying
- Hand Applied Carnauba Wax & Micro Scratch Sealant Treatment
- Dark Exterior Plastic Restoration Treatment (wherever applicable)

Package 5 [Cars $210][Trucks Vans & SUV's $299.99];The Complete Detail

- Stain Removal

Additional Options (May be applied to existing packages when requested!):

(Clay Bar Treatment): [Cars $69.99][Trucks Vans & SUV's $99.99]

- Removal of all Build-Up on Paint such as Micro debris, stone chips, water spots

(Full Vehicle Polishing): [Cars $75.99][Trucks Vans & SUV's $119.99]

- This process removes marring, swirl marks, scratches, stone chips, water spots and acid etching caused by bird droppings and bug remains.

- Adds a sleek shine when wax is applied after.

(Drizl-Q Hand Applied Window Treatment): [Cars $10.00][Trucks Vans & SUV's $15]

- This process repels water, making windshield wipers unneeded during storms and rainy weather.

A percentage of proceeds will be Donated to Help Veterans in need!

Phone #: xxx-xxx-xxxx
Email #: xxxxxxxxxx
Instagram: @
Facebook: plumebook.example/wrenautodetail
website: > Coming Soon <

Alright, that will be the first designed flyer.

The next flyer can be single paged or flyer layed out. It is generally aimed towards my first customer Calloway Wellness and Vigor. An image of there logo will be provided below along with my logo and current business card so ideas can be drawn beside them.

Wren Automotive Detailing
The Calloway Special (For August)

Package 1 [Cars $24.99][Trucks Vans & SUV's $34.99]: Speed Detail

Package 2 [Cars $39.99][Trucks Vans & SUV's $44.99]: Speed Detail & Hand Waxing

Thanks a TON! If you guy's need anymore information or have any other questions during the design process, please, please; let me know!

Target Market(s)

Automotive Detailing, Mobile Automotive Detailing, Parking Lot Detailing, Business Detailing, etc.

Industry/Entity Type

Automotive

Requirements
Must have
• A Classy Design, I'd like it to match in some form or another the Card pictures I have submitted
Nice to have
• Black and White as primary colors, silver aswell
Should not have
• Not too much Wren orange coloring in the design unless it adds to the overall definition of the finished project. Thanks!

```html
<!DOCTYPE html>
<html lang="en">
<head>
<meta charset="utf-8">
<title>The Calloway Special – Wren Automotive Detailing</title>
<link rel="stylesheet" href="https://fonts.googleapis.com/css2?family=Lato:wght@400;700;900&display=swap">
<style>
  :root {
    --page-bg: #3a3a3a;
    --flyer-black: #111112;
    --flyer-dark: #1c1c1e;
    --wren-orange: #f28a1e;
    --text-white: #ffffff;
    --silver-light: #f2f2f2;
    --silver-mid: #b9b9b9;
    --silver-dark: #7d7d7d;
    --pill-text: #141414;
  }
  * { box-sizing: border-box; margin: 0; padding: 0; }
  html, body {
    width: 1200px; height: 900px; overflow: hidden;
    background: var(--page-bg);
    font-family: "Lato", Arial, sans-serif;
  }
  .flyer {
    position: absolute; left: 313px; top: 46px;
    width: 574px; height: 808px;
    background: radial-gradient(ellipse at 50% 40%, var(--flyer-dark) 0%, var(--flyer-black) 75%);
    color: var(--text-white);
  }
  .month-tab {
    position: absolute; left: 14px; top: 12px;
    width: 29px; height: 146px; border-radius: 6px;
    background: linear-gradient(90deg, var(--silver-dark), var(--silver-light) 45%, var(--silver-mid));
    border: 1px solid #555;
    display: flex; align-items: center; justify-content: center;
  }
  .month-tab span {
    transform: rotate(-90deg); white-space: nowrap;
    font-weight: 900; font-size: 19px; color: var(--text-white);
    text-shadow: 0 1px 2px rgba(0,0,0,.6);
  }
  .title {
    position: absolute; left: 66px; top: 34px;
    font-weight: 900; font-size: 46px; line-height: 1;
    color: var(--wren-orange); letter-spacing: -0.3px;
  }
  .package {
    position: absolute; left: 59px; width: 451px;
    border: 2px solid var(--wren-orange); border-radius: 8px;
    padding: 3px 12px 0 12px;
  }
  .package--one { top: 118px; height: 218px; }
  .package--two { top: 358px; height: 248px; }
  .package-label { font-weight: 900; font-size: 19px; color: var(--wren-orange); line-height: 24px; }
  .price-bar {
    margin: 3px 0 0 -2px; width: 439px; height: 30px; border-radius: 5px;
    background: linear-gradient(180deg, var(--silver-light), var(--silver-mid) 55%, var(--silver-dark));
    border: 1px solid #444;
    box-shadow: 0 2px 3px rgba(0,0,0,.6);
    font-weight: 900; font-size: 19.5px; color: var(--pill-text);
    line-height: 28px; padding-left: 5px; white-space: nowrap;
  }
  .package-name { margin-top: 1px; font-weight: 900; font-size: 19px; color: var(--wren-orange); line-height: 24px; }
  .service-list { list-style: none; margin-top: 0; }
  .service-list li {
    position: relative; padding-left: 19px;
    font-size: 11.5px; line-height: 19.8px; color: var(--text-white);
  }
  .service-list li svg { position: absolute; left: 2px; top: 4px; width: 12px; height: 12px; }
  .donation {
    position: absolute; left: 64px; top: 636px;
    font-weight: 900; font-size: 22px; line-height: 24px; color: var(--text-white);
  }
  .partner {
    position: absolute; left: 68px; top: 742px;
    display: flex; align-items: center; gap: 8px;
    font-weight: 700; font-size: 12px; color: var(--text-white);
  }
  .partner i { width: 12px; height: 12px; background: var(--silver-mid); display: block; }
  .brand {
    position: absolute; left: 352px; top: 607px; width: 222px; height: 201px;
    display: flex; align-items: center; justify-content: center; text-align: center;
    font-weight: 900; font-size: 24px; line-height: 28px; color: var(--text-white);
  }
</style>
</head>
<body>
<svg width="0" height="0" style="position:absolute">
  <defs>
    <symbol id="burst" viewBox="0 0 12 12">
      <polygon fill="#f28a1e" points="6,0 7.2,3.4 10.2,1.8 8.6,4.8 12,6 8.6,7.2 10.2,10.2 7.2,8.6 6,12 4.8,8.6 1.8,10.2 3.4,7.2 0,6 3.4,4.8 1.8,1.8 4.8,3.4"/>
    </symbol>
  </defs>
</svg>

<main class="flyer">
  <div class="month-tab"><span>For August</span></div>
  <h1 class="title">The Calloway Special</h1>

  <section class="package package--one">
    <div class="package-label">Package 1</div>
    <div class="price-bar">[Cars $24.99][Trucks Vans &amp; SUV's $34.99]</div>
    <h2 class="package-name">Speed Detail:</h2>
    <ul class="service-list">
      <li><svg><use href="#burst"/></svg>Exterior Pressure Clean w/ Spotless water treatment and Vacuum dried</li>
      <li><svg><use href="#burst"/></svg>Wheel Wells Glossed and Cleaned</li>
      <li><svg><use href="#burst"/></svg>Tires Cleaned and Hand Dried</li>
      <li><svg><use href="#burst"/></svg>Tires Dressed with Gloss Finish</li>
      <li><svg><use href="#burst"/></svg>Exterior and Interior Windows cleaned and Hand Dried</li>
      <li><svg><use href="#burst"/></svg>Interior is Vacuumed and Door jams cleaned to Perfection!</li>
    </ul>
  </section>

  <section class="package package--two">
    <div class="package-label">Package 2</div>
    <div class="price-bar">[Cars $39.99][Trucks Vans &amp; SUV's $44.99]</div>
    <h2 class="package-name">Speed Detail &amp; Hand Waxing</h2>
    <ul class="service-list">
      <li><svg><use href="#burst"/></svg>Exterior Pressure Clean w/ Spotless water treatment and Vacuum dried</li>
      <li><svg><use href="#burst"/></svg>Wheel Wells Glossed and Cleaned</li>
      <li><svg><use href="#burst"/></svg>Tires Cleaned and Hand Dried</li>
      <li><svg><use href="#burst"/></svg>Tires Dressed with Gloss Finish</li>
      <li><svg><use href="#burst"/></svg>Exterior and Interior Windows cleaned and Hand Dried</li>
      <li><svg><use href="#burst"/></svg>Interior is Vacuumed and Door jams cleaned to Perfection!</li>
      <li><svg><use href="#burst"/></svg>Hand Applied Wax Treatment with Halvern's Advanced Spray on wax &amp;<br>Micro Scratch Sealant!</li>
    </ul>
  </section>

  <p class="donation">A percentage of proceeds<br>will be Donated to Help<br>Veterans in need!</p>

  <div class="partner"><i></i>Calloway Wellness and Vigor</div>

  <div class="brand">Wren Automotive<br>Detailing</div>
</main>
</body>
</html>
```